Redesign

Hello,

I want you to redesign this page: www.pravilo.com

I like the colors and would like to keep it 'airy', I don't want it to be the same boring website, although it needs to be easily navigational and user friendly.

NOTE: The websites main objective is to get people to signup to get our RSS services, the main task of the site is NOT a property search page, it is just a sub.

I am excited to see your designs.

Pages I am looking to have designed:
http://www.pravilo.com/
http://shortlinkory.com/q8vn27k
http://www.pravilo.com/advertise-your-real-estate.php
http://www.pravilo.com/submit-your-real-estate-listings.php
http://www.pravilo.com/2800/
http://www.pravilo.com/members/-/43

I HAVE POSTED A LARGER LOGO FOR YOU TO WORK WITH, I WANT THE LOGO TO BE INCORPORATED IN THE HEADER, NOT JUST STUCK THERE.

Owen
Updates

Hello,

I have made the project committed and I will chose one of your designs.

The current designs are nice but I really want the header to have the logo built into it, not have the logo just stuck in a box.

I also like the homepage designs with tiled sold homes, that is a great visual for the potential clients.

Thank you for your submissions so far.

Owen

Industry/Entity Type

Real Keystone

```html
<!DOCTYPE html>
<html lang="en">
<head>
<meta charset="utf-8">
<title>Pravilo — How it Works</title>
<link rel="stylesheet" href="https://fonts.googleapis.com/css2?family=Raleway:wght@300;400;500;600;700&display=swap">
<style>
:root{
  --sky-top:#2f9fe0;
  --sky-low:#b9e3fa;
  --nav:#1b78b8;
  --navy:#2b4866;
  --city-deep:#173a5a;
  --city-mid:#3f93cc;
  --dark-bar:#3e4552;
  --coral:#e66a5e;
  --cream:#fdf8cc;
  --yellow-btn:#f9c313;
  --pale-yellow:#fbe8a6;
  --pale-blue:#9fdcf8;
  --ink:#1e1e1e;
  --white:#ffffff;
  --grey:#9a9a9a;
}
*{box-sizing:border-box;margin:0;padding:0}
html,body{width:900px;height:1200px;overflow:hidden}
body{position:relative;font-family:"Raleway",sans-serif;color:var(--ink);background:var(--white)}
.abs{position:absolute}

/* header */
.site-header{left:0;top:0;width:900px;height:57px;background:linear-gradient(180deg,#1f8fd6,#54b6ee)}
.brand{left:152px;top:12px;font-size:30px;font-weight:600;color:var(--white);display:flex;align-items:center;gap:8px}
.brand-dot{width:10px;height:10px;border-radius:50%;background:var(--yellow-btn)}
.role-btn{top:13px;height:26px;width:82px;border-radius:4px;font-size:11px;font-weight:500;display:flex;align-items:center;justify-content:center;gap:10px;color:var(--ink)}
.role-btn.buyers{left:577px;background:var(--pale-yellow)}
.role-btn.sellers{left:668px;background:var(--pale-blue)}
.caret{width:0;height:0;border-left:4px solid transparent;border-right:4px solid transparent;border-top:5px solid var(--ink)}
.main-nav{left:0;top:57px;width:900px;height:23px;background:var(--nav);display:flex;align-items:center}
.main-nav a{color:var(--white);font-size:9px;font-weight:600;text-decoration:none;padding:0 15px;border-right:1px solid rgba(255,255,255,.3)}
.main-nav a:first-child{margin-left:135px}
.main-nav a:last-of-type{border-right:0}
.social{left:626px;top:59px;display:flex;gap:6px}
.social span{width:18px;height:18px;border-radius:50%;background:var(--navy);border:1px solid rgba(255,255,255,.5)}

/* hero */
.hero{left:0;top:80px;width:900px;height:282px;overflow:hidden;
  background:
    radial-gradient(ellipse 120px 40px at 70px 10px,rgba(255,255,255,.9),rgba(255,255,255,0)),
    radial-gradient(ellipse 110px 45px at 830px 50px,rgba(255,255,255,.9),rgba(255,255,255,0)),
    radial-gradient(ellipse 90px 30px at 330px 30px,rgba(255,255,255,.5),rgba(255,255,255,0)),
    linear-gradient(180deg,var(--sky-top) 0%,#7dcbf3 55%,var(--sky-low) 100%)}
.hero-title{left:0;top:20px;width:900px;text-align:center;font-size:38px;font-weight:300;color:var(--ink)}
.steps{left:0;top:0}
.skyline{left:148px;top:195px;width:602px;height:87px;
  background:linear-gradient(180deg,rgba(63,147,204,0) 0%,rgba(63,147,204,.55) 30%,var(--city-mid) 55%,var(--city-deep) 100%)}

/* search */
.search-band{left:0;top:362px;width:900px;height:43px;background:var(--dark-bar)}
.city-select{left:150px;top:10px;width:106px;height:23px;background:var(--white);border-radius:2px 0 0 2px;font-size:10px;color:#555;display:flex;align-items:center;justify-content:space-between;padding:0 10px 0 13px;border-right:1px solid #ddd}
.city-select .caret{border-top-color:#555}
.locality{left:256px;top:10px;width:401px;height:23px;background:var(--white);border-radius:0 2px 2px 0;font-size:10px;color:#aaa;display:flex;align-items:center;gap:8px;padding-left:10px}
.search-btn{left:666px;top:10px;width:84px;height:23px;background:var(--yellow-btn);border-radius:2px;font-size:11px;font-weight:600;display:flex;align-items:center;justify-content:center;gap:6px}

/* listings */
.listings{left:0;top:405px;width:900px;height:241px;background:var(--coral)}
.section-title{width:900px;left:0;text-align:center;font-weight:300;font-size:20px}
.listings .section-title{top:20px;color:var(--white)}
.card{top:57px;width:183px;height:175px;background:var(--cream)}
.card-photo{left:7px;top:7px;width:168px;height:74px}
.photo-building{background:linear-gradient(180deg,#7fb6e0,#c8c59a 60%,#4c6b36)}
.photo-room{background:linear-gradient(180deg,#6b3f22,#c28a55 55%,#efe3cf)}
.photo-street{background:linear-gradient(180deg,#7f8a8c,#5c5a52 60%,#3d4a36)}
.view-details{left:50px;top:26px;width:90px;height:22px;background:var(--coral);border-radius:3px;color:var(--white);font-size:8.5px;display:flex;align-items:center;justify-content:center;gap:5px}
.card-title{left:8px;top:89px;width:170px;font-size:7.5px;line-height:12px;color:var(--ink)}
.card-price{left:9px;top:118px;font-size:9px;font-weight:700;color:var(--coral)}
.timer-labels{top:143px;right:10px;display:flex;gap:11px;font-size:6.5px;color:var(--grey)}
.timer{top:151px;right:10px;display:flex;align-items:center;gap:2px}
.timer b{width:13px;height:14px;border-radius:2px;background:var(--dark-bar);color:var(--white);font-size:7.5px;display:flex;align-items:center;justify-content:center}
.timer i{font-style:normal;font-size:8px;color:var(--coral);padding:0 1px}

/* brands */
.brands{left:0;top:646px;width:900px;height:160px;background:var(--white)}
.brands .section-title{top:27px;color:var(--ink);font-size:21px}
.brand-row{left:185px;top:90px;width:530px;height:40px;display:flex;align-items:center;justify-content:space-between}
.partner{display:flex;align-items:center;gap:5px;font-size:13px;font-weight:700;color:#4a4a4a;letter-spacing:.5px}
.partner span{width:14px;height:14px;background:#6a6a6a}
.partner.blue{color:#1d4f9c}
.partner.blue span{background:#1d4f9c}

/* testimonials */
.testimonials{left:0;top:806px;width:900px;height:354px;background:linear-gradient(180deg,#f6c126,#f1b51c)}
.testimonials .section-title{top:28px;color:var(--ink);font-size:20px}
.quote{top:75px;width:170px;height:126px;background:var(--white);border-radius:12px;padding:27px 10px 0 11px;font-size:8.8px;line-height:14.5px;color:#333}
.quote-tail{top:200px}
.person{top:235px;display:flex;align-items:center;gap:12px}
.avatar{width:40px;height:40px;border-radius:50%;background:#d9d4cc;border:2px solid var(--white)}
.person p{font-size:8.8px;line-height:14px;color:var(--ink)}
.person strong{font-weight:700}
.read-all{left:379px;top:302px;width:146px;height:31px;border:1.5px solid var(--ink);border-radius:4px;font-size:10.5px;display:flex;align-items:center;justify-content:center}

/* footer */
.site-footer{left:0;top:1160px;width:900px;height:40px;background:var(--coral)}
.copyright{left:150px;top:16px;font-size:7px;color:var(--white)}
.footer-brand{left:665px;top:7px;font-size:22px;font-weight:600;color:var(--white)}
</style>
</head>
<body>

<header class="abs site-header">
  <div class="abs brand">Pravilo<span class="brand-dot"></span></div>
  <div class="abs role-btn buyers">BUYERS <span class="caret"></span></div>
  <div class="abs role-btn sellers">SELLERS <span class="caret"></span></div>
</header>
<nav class="abs main-nav">
  <a href="#">Advertise Your Properties</a>
  <a href="#">FAQS</a>
  <a href="#">Contact Us</a>
</nav>
<div class="abs social" aria-label="Social links"><span></span><span></span><span></span><span></span><span></span></div>

<section class="abs hero">
  <h1 class="abs hero-title">How it Works?</h1>
  <div class="abs skyline" role="img" aria-label="City skyline of blue towers with a walker and a cyclist in the street"></div>
  <svg class="abs steps" width="900" height="282" viewBox="0 0 900 282">
    <path d="M150 222 C170 200,185 200,204 195 C250 180,290 180,333 175 C380 170,420 168,478 163 C540 157,580 150,618 134 C650 120,680 100,700 85"
      fill="none" stroke="#1f6fae" stroke-width="1.2" stroke-dasharray="3 3"/>
    <circle cx="208" cy="141" r="8" fill="none" stroke="#1c3d5e" stroke-width="3"/>
    <line x1="202" y1="147" x2="190" y2="159" stroke="#1c3d5e" stroke-width="4" stroke-linecap="round"/>
    <circle cx="367" cy="124" r="17" fill="none" stroke="#1c3d5e" stroke-width="3"/>
    <path d="M367 113 V124 H375" fill="none" stroke="#1c3d5e" stroke-width="2.5"/>
    <text x="505" y="107" font-family="Raleway,sans-serif" font-size="20" font-weight="700" fill="#1c3d5e" text-anchor="middle">$</text>
    <rect x="483" y="113" width="44" height="10" rx="5" fill="#1c3d5e"/>
    <path d="M614 86 L628 74 L640 84 L652 72" fill="none" stroke="#1c3d5e" stroke-width="4" stroke-linecap="round" stroke-linejoin="round"/>
    <path d="M692 88 L708 78 L700 92 Z" fill="#1f6fae"/>
    <g font-family="Raleway,sans-serif" font-weight="700" font-size="15" fill="#5bc6f5" text-anchor="middle">
      <circle cx="204" cy="195" r="15" fill="#2b4866"/><text x="204" y="200">1</text>
      <circle cx="333" cy="175" r="15" fill="#2b4866"/><text x="333" y="180">2</text>
      <circle cx="478" cy="163" r="15" fill="#2b4866"/><text x="478" y="168">3</text>
      <circle cx="618" cy="134" r="15" fill="#2b4866"/><text x="618" y="139">4</text>
    </g>
    <g font-family="Raleway,sans-serif" font-weight="600" font-size="8.8" fill="#2b4866" text-anchor="middle">
      <text x="201" y="173">Search Current Listings</text>
      <text x="367" y="157">Make an offer</text>
      <text x="506" y="146">Negotiate</text>
      <text x="637" y="107">Close the Deal</text>
    </g>
  </svg>
</section>

<section class="abs search-band">
  <div class="abs city-select">Select City <span class="caret"></span></div>
  <div class="abs locality">
    <svg width="9" height="12" viewBox="0 0 9 12"><path d="M4.5 0A4.5 4.5 0 0 0 0 4.5C0 8 4.5 12 4.5 12S9 8 9 4.5A4.5 4.5 0 0 0 4.5 0Z" fill="#bbb"/><circle cx="4.5" cy="4.5" r="1.6" fill="#fff"/></svg>
    Enter locality or project or builder
  </div>
  <div class="abs search-btn">
    <svg width="11" height="11" viewBox="0 0 11 11"><circle cx="4.5" cy="4.5" r="3.5" fill="none" stroke="#1e1e1e" stroke-width="1.6"/><line x1="7" y1="7" x2="10" y2="10" stroke="#1e1e1e" stroke-width="1.8"/></svg>
    SEARCH
  </div>
</section>

<section class="abs listings">
  <h2 class="abs section-title">CURRENT PROPERTIES LISTINGS</h2>

  <article class="abs card" style="left:9px">
    <div class="abs card-photo photo-building" role="img" aria-label="Apartment building exterior"></div>
    <p class="abs card-title">3 BHK, Independent/Builder Floor for Sale<br>in Mesa, AZ</p>
    <p class="abs card-price">$164,900</p>
    <div class="abs timer-labels"><span>Hours</span><span>Minutes</span><span>Seconds</span></div>
    <div class="abs timer"><b>0</b><b>1</b><i>:</i><b>1</b><b>1</b><i>:</i><b>4</b><b>6</b></div>
  </article>

  <article class="abs card" style="left:199px">
    <div class="abs card-photo photo-room" role="img" aria-label="Furnished living room interior"></div>
    <p class="abs card-title">3 BHK, Independent/Builder Floor for Sale<br>in MIMS, FL</p>
    <p class="abs card-price">$124,900</p>
    <div class="abs timer-labels"><span>Hours</span><span>Minutes</span><span>Seconds</span></div>
    <div class="abs timer"><b>2</b><b>0</b><i>:</i><b>1</b><b>0</b><i>:</i><b>3</b><b>0</b></div>
  </article>

  <article class="abs card" style="left:390px">
    <div class="abs card-photo photo-street" role="img" aria-label="Residential building with palm trees"></div>
    <div class="abs view-details">
      <svg width="14" height="8" viewBox="0 0 14 8"><path d="M0 4C3-1 11-1 14 4C11 9 3 9 0 4Z" fill="#fff"/><circle cx="7" cy="4" r="2" fill="#e66a5e"/></svg>
      View Details
    </div>
    <p class="abs card-title">2 BHK, 3 BHK Independent Floor for Sale<br>in Brandon, FL</p>
    <p class="abs card-price">$104,900</p>
    <div class="abs timer-labels"><span>Hours</span><span>Minutes</span><span>Seconds</span></div>
    <div class="abs timer"><b>0</b><b>1</b><i>:</i><b>1</b><b>5</b><i>:</i><b>1</b><b>6</b></div>
  </article>

  <article class="abs card" style="left:581px">
    <div class="abs card-photo photo-building" role="img" aria-label="Apartment building exterior"></div>
    <p class="abs card-title">3 BHK, Independent/Builder Floor for Sale<br>in Brandon, FL</p>
    <p class="abs card-price">$164,100</p>
    <div class="abs timer-labels"><span>Hours</span><span>Minutes</span><span>Seconds</span></div>
    <div class="abs timer"><b>0</b><b>1</b><i>:</i><b>1</b><b>1</b><i>:</i><b>4</b><b>6</b></div>
  </article>

  <article class="abs card" style="left:771px">
    <div class="abs card-photo photo-room" role="img" aria-label="Furnished living room interior"></div>
    <p class="abs card-title">3 BHK, Independent/Builder Floor for Sale<br>in Brandon, FL</p>
    <p class="abs card-price">$144,900</p>
    <div class="abs timer-labels" style="right:auto;left:72px"><span>Hours</span><span>Minutes</span></div>
    <div class="abs timer" style="right:auto;left:70px"><b>2</b><b>0</b><i>:</i><b>1</b><b>0</b></div>
  </article>
</section>

<section class="abs brands">
  <h2 class="abs section-title">POPULAR REAL ESTATE BRANDS</h2>
  <svg class="abs" style="left:150px;top:106px" width="18" height="10" viewBox="0 0 18 10"><path d="M17 5H3M7 1L2 5L7 9" fill="none" stroke="#bbb" stroke-width="2"/></svg>
  <div class="abs brand-row">
    <div class="partner"><span></span>RIDGELINE REALTY</div>
    <div class="partner blue"><span></span>SIERRA</div>
    <div class="partner">HOLLIS HOMES</div>
    <div class="partner"><span></span>KEYSTONE</div>
    <div class="partner" style="color:#999">CORBEL</div>
  </div>
  <svg class="abs" style="left:732px;top:106px" width="18" height="10" viewBox="0 0 18 10"><path d="M1 5H15M11 1L16 5L11 9" fill="none" stroke="#e66a5e" stroke-width="2"/></svg>
</section>

<section class="abs testimonials">
  <h2 class="abs section-title">WHAT OUR CUSTOMER THINKS ...</h2>

  <blockquote class="abs quote" style="left:150px">'The Best quality Lorem ipsum Ever!! dolor sit amet, consecutor adispicing elit. Aliquam at portitior sem. Aliquam erat volupat condimentum sed!'</blockquote>
  <svg class="abs quote-tail" style="left:205px" width="50" height="40" viewBox="0 0 50 40"><path d="M20 0H48L0 40Z" fill="#fff"/></svg>
  <div class="abs person" style="left:160px"><div class="avatar"></div><p><strong>Lena Marsh,</strong><br>Sector 1, Los Angeles</p></div>

  <blockquote class="abs quote" style="left:366px">'The Best quality Lorem ipsum Ever!! dolor sit amet, consecutor adispicing elit. Aliquam at portitior sem. Aliquam erat volupat condimentum sed!'</blockquote>
  <svg class="abs quote-tail" style="left:420px" width="50" height="40" viewBox="0 0 50 40"><path d="M20 0H48L0 40Z" fill="#fff"/></svg>
  <div class="abs person" style="left:374px"><div class="avatar"></div><p><strong>Arun Mehta,</strong><br>London</p></div>

  <blockquote class="abs quote" style="left:582px">'The Best quality Lorem ipsum Ever!! dolor sit amet, consecutor adispicing elit. Aliquam at portitior sem. Aliquam erat volupat condimentum sed!'</blockquote>
  <svg class="abs quote-tail" style="left:636px" width="50" height="40" viewBox="0 0 50 40"><path d="M20 0H48L0 40Z" fill="#fff"/></svg>
  <div class="abs person" style="left:591px"><div class="avatar"></div><p><strong>Dev Kapoor,</strong><br>Canada</p></div>

  <div class="abs read-all">READ ALL TESTIMONIALS</div>
</section>

<footer class="abs site-footer">
  <p class="abs copyright">Copyright © 2014 Pravilo. All Rights Reserved.</p>
  <div class="abs footer-brand">Pravilo</div>
</footer>

</body>
</html>
```